Prosthetic Brochure

Looking for a trifold brochure that highlights our Prosthetic department. Has to have good stock pictures of prosthetic care. Should have Prosthetic Services from our website www.brindlemoorclinic.com I would like it in the same colors of our website.

Target Market(s)

Patients and physicians

Industry/Entity Type

Medical

Requirements
Must have
• Pictures of people helping prosthetic patients and information from the flyer I uploaded and our website under Prosthetic services.
Nice to have
• Same color scheme as our website. Blue with orange highlights
Should not have
• Just prosthetics no pictures of braces ( orthotics)

```html
<!DOCTYPE html>
<html lang="en">
<head>
<meta charset="utf-8">
<title>Brindlemoor Clinic – Prosthetic Brochure</title>
<link href="https://fonts.googleapis.com/css2?family=Arimo:wght@400;700&family=Playfair+Display:ital,wght@1,700&display=swap" rel="stylesheet">
<style>
  :root{
    --orange:#f47b20;
    --ink:#1a1a1a;
    --white:#ffffff;
    --blue-top:#0a74c2;
    --blue-bottom:#0b3b7c;
    --photo-light:#d9d9d9;
    --photo-dark:#6f6f6f;
  }
  *{margin:0;padding:0;box-sizing:border-box}
  html,body{width:1200px;height:848px;overflow:hidden;background:var(--white)}
  .spread{position:relative;width:1200px;height:848px;font-family:"Arimo",Arial,sans-serif;color:var(--ink)}

  /* left panel */
  .why-panel{position:absolute;left:0;top:0;width:405px;height:848px;background:var(--white);overflow:hidden}
  .why-title{position:absolute;left:53px;top:50px;font-family:"Playfair Display",Georgia,serif;font-style:italic;font-weight:700;font-size:33px;line-height:40px;letter-spacing:-0.5px;white-space:nowrap}
  .why-title .accent{color:var(--orange)}
  .benefits{position:absolute;left:53px;top:145px;width:312px;list-style:none}
  .benefit{margin-bottom:10px}
  .benefit h3{font-size:16px;font-weight:700;color:var(--orange);line-height:20px}
  .benefit h3::before{content:"➜";margin-right:5px}
  .benefit p{font-size:15.4px;line-height:18.8px;padding-left:19px}
  .closing{position:absolute;left:52px;top:633px;width:300px;font-size:15.8px;font-weight:700;line-height:19px;color:var(--orange)}
  .device-art{position:absolute;left:51px;top:705px;width:307px;height:70px;background:linear-gradient(90deg,#ececec,#f6f6f6,#ececec);border-radius:4px}
  .site-url{position:absolute;left:52px;top:784px;font-size:15.6px}

  /* right panel */
  .team-panel{position:absolute;left:405px;top:0;width:795px;height:848px;background:linear-gradient(180deg,var(--blue-top) 0%,var(--blue-bottom) 100%)}
  .team-title{position:absolute;left:46px;top:44px;font-family:"Playfair Display",Georgia,serif;font-style:italic;font-weight:700;font-size:41px;color:var(--white);letter-spacing:-0.5px;white-space:nowrap}
  .team-title .accent{color:var(--orange)}

  .member{position:absolute;width:320px}
  .member .name{position:absolute;left:111px;top:0;width:169px;height:21px;background:var(--orange);color:var(--white);font-size:13.5px;line-height:21px;text-align:center;white-space:nowrap}
  .member .photo{position:absolute;left:0;top:5px;width:141px;height:141px;border-radius:50%;border:3px solid var(--white);background:radial-gradient(circle at 50% 40%,var(--photo-light),var(--photo-dark))}
  .member .bio{position:absolute;left:0;top:30px;width:320px;color:var(--white);font-size:13.2px;line-height:14.2px}
  .member .wrap{float:left;width:150px;height:124px;shape-outside:circle(72px at 70px 46px);shape-margin:12px}
  .member .cred{margin-bottom:14px}

  .col-a{left:46px}
  .col-b{left:452px}
  .row-1{top:123px}
  .row-2{top:352px}
  .row-3{top:602px}
</style>
</head>
<body>
<div class="spread">

  <section class="why-panel">
    <h1 class="why-title">Why use <span class="accent">Brindlemoor</span><br><span class="accent">Clinic?</span></h1>
    <ul class="benefits">
      <li class="benefit"><h3>First-class patient care</h3><p>Our Facility is accredited by the National Board for Certification in Prosthetics and Orthotics. We have met rigid standards that put patient needs and safety first.</p></li>
      <li class="benefit"><h3>High-end technology</h3><p>We are always current on the latest socket and component technology.</p></li>
      <li class="benefit"><h3>Local Fabrication Facility</h3><p>Our fabrication and assembly happens right here in St. Louis.</p></li>
      <li class="benefit"><h3>Experience</h3><p>78 years of combined technical and practitioner experience.</p></li>
      <li class="benefit"><h3>Fast turnaround</h3><p>Same week check sockets, complete definitive prosthesis in 30 days ( pending insurance authorizations).</p></li>
      <li class="benefit"><h3>A firm belief in teamwork</h3><p>We love to work with the patient, rehabilitative staff and physicians to achieve the patient’s goals.</p></li>
    </ul>
    <p class="closing">ALL OF THESE SERVICES COMBINED ALLOW US TO PROVIDE THE BEST POSSIBLE PATIENT OUTCOME.</p>
    <div class="device-art" role="img" aria-label="Row of light grey line illustrations of prosthetic limbs and hands"></div>
    <p class="site-url">www.brindlemoorclinic.com</p>
  </section>

  <section class="team-panel">
    <h2 class="team-title"><span class="accent">Our Team</span> of Experts</h2>

    <article class="member col-a row-1">
      <div class="photo" role="img" aria-label="Portrait photo of Daniel Hollis"></div>
      <div class="name">DANIEL HOLLIS, CPO</div>
      <div class="bio"><div class="wrap"></div>
        <p class="cred">National Board Certified<br>Prosthetist &amp; Orthotist</p>
        <p>Daniel has dual Master’s Degrees in Prosthetics and Orthotic and in Business Administration. His undergrad was in Athletic training. Daniel is up to date on the latest cutting edge prosthetic technology and loves the advancements being made in prosthetics.</p>
      </div>
    </article>

    <article class="member col-b row-1">
      <div class="photo" role="img" aria-label="Portrait photo of Martin Keller"></div>
      <div class="name">MARTIN KELLER, CPO</div>
      <div class="bio"><div class="wrap"></div>
        <p class="cred">National Board Certified<br>Prosthetist &amp; Orthotist</p>
        <p>With over 46 years of prosthetic experience, Martin has been a leader and past president of our National organization and is highly respected for his experience and knowledge.</p>
      </div>
    </article>

    <article class="member col-a row-2">
      <div class="photo" role="img" aria-label="Portrait photo of Laura Brenner"></div>
      <div class="name">LAURA BRENNER, CPO</div>
      <div class="bio"><div class="wrap"></div>
        <p class="cred">National Board Certified<br>Prosthetist &amp; Orthotist</p>
        <p>Laura graduated from Harlow State University with her Master of Science in Prosthetics and Orthotics. She has been practicing Prosthetics and Orthotics since 2018. Laura is a people person and loves working with patients.</p>
      </div>
    </article>

    <article class="member col-b row-2">
      <div class="photo" role="img" aria-label="Portrait photo of Nora Whitfield"></div>
      <div class="name">NORA WHITFIELD, CPO</div>
      <div class="bio"><div class="wrap"></div>
        <p class="cred">National Board Certified<br>Prosthetist &amp; Orthotist</p>
        <p>Nora graduated from Eastmere University with her Masters Degree in Prosthetics &amp; Orthotics. Nora did her undergrad at BRU in biomedical Engineering. Nora is a St. Louis native and loves this city.</p>
      </div>
    </article>

    <article class="member col-a row-3">
      <div class="photo" role="img" aria-label="Portrait photo of Evan Rourke"></div>
      <div class="name">EVAN ROURKE, CPO</div>
      <div class="bio"><div class="wrap"></div>
        <p class="cred">National Board Certified<br>Prosthetist &amp; Orthotist</p>
        <p>Evan grew up in St. Louis and went to BRU where he graduated in biomedical engineering. He graduated from Texas Southbrook with a Masters Degree in Prosthetics and Orthotics. His hobbies include playing soccer and he is passionate about helping others.</p>
      </div>
    </article>

    <article class="member col-b row-3">
      <div class="photo" role="img" aria-label="Portrait photo of Owen Pratley"></div>
      <div class="name">OWEN PRATLEY, CPO</div>
      <div class="bio"><div class="wrap"></div>
        <p class="cred">National Board Certified<br>Orthotist &amp; NPCE<br>Prosthetist</p>
        <p>Owen graduated from the University of Ferndale with a Master Degree in Prosthetics and Orthotics. His undergrad is in exercise physiology from Calloway State. Owen is a huge outdoor enthusiast and loves helping people regain their independence.</p>
      </div>
    </article>
  </section>

</div>
</body>
</html>
```